business card with logo Velmora Nails & Spa 2816 SW Quillan Ave Portland OR 97384

Would like to have a business card with our logo.
like bottle of polish with our logo or letter V on it
want something that first glance would let you know that it is a nail salon.
like the hands with polish bottle dripping.
like black or White back ground

Velmora Nails & Spa
(The Velvet Retreat)
2816 SW Quillan Ave
Portland, OR 97384
Call or Text: 1-503-555-0148
www.VelmoraNailsnSpa.example
Open 7 days a week.
After 7:00 PM is by appointment only.
Closed only on Thanksgiving & Christmas.

Target Market(s)

20%Man and 80%Woman 13-70

Industry/Entity Type

Business

Contact Information for Business Card

Elegant with Logo-Business name- address-phone-open days. closed day.

Font styles to use
Decorative
Script

Colors
000000

Requirements
Must have
• Logo and place for Technician Name
• Velmora Nails & Spa
• (The Velvet Retreat)
• 2816 SW Quillan Ave
• Portland, OR 97384
• Call or Text: 1-503-555-0148
• Open 7 days a week
• Closed only on Thanksgiving & Christmas.
• We accepted all major credit cards but prefer cash. Thank you
Nice to have
• Nail polish bottle with our Logo or letter V
Should not have
• too colorful

```html
<!DOCTYPE html>
<html lang="en">
<head>
<meta charset="utf-8">
<title>Velmora Nails &amp; Spa – Business Card</title>
<link rel="stylesheet" href="https://fonts.googleapis.com/css2?family=Arimo:ital,wght@0,400;0,700;1,400;1,700&family=Italianno&display=swap">
<style>
  :root {
    --ink: #1c1c1c;
    --ink-soft: #3a3a3a;
    --grey: #707070;
    --grey-light: #9a9a9a;
    --paper: #ffffff;
    --wash: #e6e6e6;
    --wash-deep: #c9c9c9;
  }
  * { margin: 0; padding: 0; box-sizing: border-box; }
  html, body { width: 686px; height: 1200px; overflow: hidden; background: var(--paper); }
  .card {
    position: relative;
    width: 686px; height: 1200px;
    background: var(--paper);
    font-family: "Arimo", Arial, sans-serif;
    color: var(--ink);
    overflow: hidden;
  }
  .wash {
    position: absolute;
    right: -60px; top: 340px;
    width: 580px; height: 760px;
    background: radial-gradient(ellipse at 62% 30%, var(--wash-deep) 0%, var(--wash) 32%, rgba(255,255,255,0) 68%);
    opacity: .8;
  }
  .brand {
    position: absolute;
    left: 0; right: 0; top: 128px;
    text-align: center;
    font-weight: 400;
    color: var(--ink);
  }
  .brand__name { font-size: 92px; line-height: 100px; letter-spacing: 2px; }
  .brand__sub { font-size: 40px; line-height: 50px; margin-top: 6px; }
  .bottle-photo {
    position: absolute;
    left: 74px; top: 394px;
    width: 204px; height: 384px;
    background: linear-gradient(160deg, #ffffff 0%, #eeeeee 55%, #d6d6d6 100%);
    border-radius: 18px;
  }
  .details {
    position: absolute;
    right: 77px; top: 582px;
    text-align: right;
  }
  .tech-name { font-weight: 700; font-size: 40px; line-height: 46px; color: var(--ink-soft); }
  .tech-role {
    font-family: "Italianno", cursive;
    font-size: 30px; letter-spacing: 5px; line-height: 34px; color: var(--ink-soft);
  }
  .call-label { font-size: 30px; color: var(--grey); margin-top: 10px; line-height: 34px; }
  .phone { font-size: 42px; color: var(--ink); line-height: 48px; }
  .salon { font-size: 23px; margin-top: 16px; line-height: 27px; }
  .salon-sub { font-size: 19px; color: var(--grey); line-height: 27px; }
  .address { font-size: 20px; color: var(--grey); line-height: 27px; }
  .hours { font-size: 24px; line-height: 34px; margin-top: 14px; color: var(--ink-soft); }
  .hours b { color: var(--ink); }
  .hours .closed { font-style: italic; color: var(--grey); }
  .hours .closed b { color: var(--ink-soft); }
  .payment-note { font-size: 19px; line-height: 25px; margin-top: 16px; color: var(--ink-soft); }
  .payment-methods {
    display: flex; justify-content: flex-end; gap: 12px;
    margin-top: 14px;
  }
  .method {
    display: flex; align-items: center; gap: 5px;
    font-size: 15px; font-weight: 700; color: var(--ink-soft);
  }
  .method::before {
    content: ""; width: 14px; height: 14px; background: var(--grey-light);
  }
  .website {
    position: absolute;
    left: 0; right: 0; top: 1124px;
    text-align: center;
    font-family: "Italianno", cursive;
    font-size: 28px; letter-spacing: 6px;
    color: var(--ink-soft);
  }
</style>
</head>
<body>
  <div class="card">
    <div class="wash" role="img" aria-label="Soft grey watercolour wash"></div>

    <div class="brand">
      <div class="brand__name">Velmora</div>
      <div class="brand__sub">Nails &amp; Spa</div>
    </div>

    <div class="bottle-photo" role="img" aria-label="White nail polish bottle carrying the salon name"></div>

    <div class="details">
      <div class="tech-name">Marissa Dole</div>
      <div class="tech-role">Nail Technician</div>
      <div class="call-label">Call / Text</div>
      <div class="phone">1-503-555-0148</div>

      <div class="salon">Velmora Nails &amp; Spa</div>
      <div class="salon-sub">(The Velvet Retreat)</div>
      <div class="address">2816 SW Quillan Ave Portland, OR 97384</div>

      <div class="hours">
        <div>Open <b>7 days</b> a week</div>
        <div>After <b>7:00 PM</b> is by <b>appointment only</b></div>
        <div class="closed"><b>Closed</b> only on <b>Thanksgiving &amp; Christmas</b></div>
      </div>

      <div class="payment-note">We accepted all major credit<br>cards but prefer cash. Thank you</div>
      <div class="payment-methods">
        <span class="method">Payvo</span>
        <span class="method">Cardmark</span>
        <span class="method">Tallis</span>
        <span class="method">Dovex</span>
      </div>
    </div>

    <div class="website">www.VelmoraNailsnSpa.example</div>
  </div>
</body>
</html>
```